To design the Curriculum Vitae of a General Manager Legal

the objective is to redesign the attached Résumé for a senior level Internal Legal Executive in order to make it attractive, easily readable, catchy, modern looking while staying classy, elegant, sobre, and serious.
The résumé is attached to this project. it contains the followings sections : Photo; Contact Details; Summary; Education; Experience; Other.
Feel free to use photoshop to improve photo.
Updates

Target Market(s)

Legal community; law firms; Big corporations requiring internal legal senior executive

Font styles to use
Serif

Colors
ffffff
85cae6
33a6d7
0292cd
86cfc6
cfeae6
757575
919191
d9d9d9

Requirements
Must have
• classy; serious; professional; elegant; easy to read; catchy; modern;

```html
<!DOCTYPE html>
<html lang="en">
<head>
<meta charset="utf-8">
<title>Curriculum Vitae – Page 3</title>
<link href="https://fonts.googleapis.com/css2?family=Gentium+Book+Plus:wght@400;700&family=Open+Sans&display=swap" rel="stylesheet">
<style>
  :root {
    --paper: #ffffff;
    --ink: #1c1c1c;
    --side-band: #d9d9d9;
    --bullet: #85cae6;
    --muted: #333333;
  }
  * { margin: 0; padding: 0; box-sizing: border-box; }
  html, body { width: 927px; height: 1200px; overflow: hidden; background: var(--paper); }
  body {
    position: relative;
    font-family: "Gentium Book Plus", "Palatino Linotype", Palatino, serif;
    font-size: 15px;
    line-height: 19px;
    color: var(--ink);
  }
  .side-band {
    position: absolute;
    left: 14px; top: 12px;
    width: 30px; height: 1176px;
    background: var(--side-band);
  }
  .page-content {
    position: absolute;
    left: 110px; top: 79px;
    width: 744px;
  }
  .bullet-list { list-style: none; padding-left: 27px; }
  .bullet-list li { position: relative; margin-bottom: 8px; }
  .bullet-list li::before {
    content: "";
    position: absolute;
    left: -18px; top: 7px;
    width: 5px; height: 5px;
    border-radius: 50%;
    background: var(--bullet);
  }
  .section-title {
    font-weight: 700;
    margin: 37px 0 18px;
  }
  .role-title {
    font-weight: 700;
    margin: 37px 0 18px;
  }
  .role-title .dates { margin-right: 10px; }
  .role-summary { text-align: justify; margin-bottom: 0; }
  .page-number {
    position: absolute;
    right: 29px; top: 1151px;
    font-family: "Open Sans", Arial, sans-serif;
    font-size: 14px;
    color: var(--muted);
  }
</style>
</head>
<body>
  <div class="side-band"></div>

  <main class="page-content">
    <ul class="bullet-list">
      <li>Communicate latest regulatory requirements to Business Units</li>
      <li>Develop and maintain legal processes and business transactions compliance and related training; Provide support for governmental relations and regulatory affairs activities.</li>
    </ul>

    <h2 class="section-title">Risk Management</h2>
    <ul class="bullet-list">
      <li>Lead implementation of risk control measures, contractual obligations and structuring of transactions.</li>
      <li>Manage legal risks and provide alternative solutions to minimize liability exposure while achieving business goals.</li>
    </ul>

    <h2 class="section-title">Other</h2>
    <ul class="bullet-list">
      <li>Review and negotiate (in conjunction with Treasury department) of financial documentation required to satisfy funding, banking and other monetary services’ requirements of the company;</li>
      <li>For new jurisdictions: Carry out legal research, due diligence procedures, prepare corporate documents and other formalities for relevant operating companies. Establish methods to accomplish business goals while minimizing legal and commercial risks.</li>
      <li>Prepare board presentations and on-going updates to senior management</li>
    </ul>

    <h2 class="role-title"><span class="dates">Nov 2011 - May 2015</span> Legal Counsel at Al Noor Estates LLC (“ANE”) - Dubai</h2>
    <p class="role-summary">Lead and manage legal functions related to the UAE shopping malls of ANE in Dubai, Ajman, Sharjah, and Fujairah (Development, JVs, land acquisitions, asset management, leasing construction and project management).</p>
    <ul class="bullet-list">
      <li style="margin-bottom:0">limited to leasing, procurement, operation, marketing, construction, development, consultancy, IT and HR.</li>
      <li>Provided legal advice and opinions on matters pertaining to the business of ANE and compliance with UAE laws.</li>
      <li>Handled mall litigation cases, sending out legal notices, filing cases and preparing memos, preparing settlement agreements, referring disputes to external lawyers when necessary, and managing and following up with lawyers until complete execution of judgments.</li>
      <li>Negotiated with outside parties along with relevant internal clients for finalizing commercial deals relating to the malls and preparing the required legal documents accordingly.</li>
      <li>Attending to relevant local authorities to obtain information and updates where required and to lobby and submit requests relating to the business requirements of ANE.</li>
      <li>Prepared various agreements related to business development of ANE in the UAE and the MENA Region (Joint Ventures, Sale and Purchase Agreements, Usufruct Agreements, Moustaha Agreements …etc.).</li>
      <li>Participated in negotiating and preparation of contracts related to development, design and construction of shopping malls in various countries in the MENA region (FIDIC, D&amp;B…etc.).</li>
      <li>Participated in preparation of legal documents and liaising with external lawyers in arbitration cases.</li>
      <li>Preparation of board presentations and updates to senior management.</li>
      <li>Participated in the preparation of legal documentation and contracts relating to development, design, operation, selling of residences and management of a real estate community in the Emirate of Sharjah.</li>
      <li>Provided internal training on adapting standard templates and legal documents.</li>
    </ul>
  </main>

  <div class="page-number">3</div>
</body>
</html>
```